Catering company needs business cards

We need new business cards for growing catering company.

Industry/Entity Type

Business

Requirements
Must have
• Company logo
• Marisol Quedenfeldt
• Catering Director
• marisol.t.quedenfeldt-1@orvanta-mail.org
• 407-555-0182
• 407-555-0267
• Building R2-718 PTX
• Brightwater Launch Campus
• Florida, 33741

```html
<!DOCTYPE html>
<html lang="en">
<head>
<meta charset="utf-8">
<title>Highfield Catering Company – Business Card</title>
<link href="https://fonts.googleapis.com/css2?family=Lato:wght@400;700&display=swap" rel="stylesheet">
<style>
  :root {
    --page-bg: #e9eaec;
    --brand-blue: #1f6fae;
    --brand-blue-dark: #15548c;
    --brand-blue-light: #2a82c4;
    --card-white: #ffffff;
    --card-grey: #eceded;
    --ink: #1d1d1f;
    --rule: #6d9ccb;
  }
  * { margin: 0; padding: 0; box-sizing: border-box; }
  html, body { width: 1200px; height: 900px; overflow: hidden; }
  body {
    background: var(--page-bg);
    font-family: "Lato", "Gill Sans", sans-serif;
    position: relative;
  }
  .card {
    position: absolute;
    left: 285px;
    width: 630px;
    height: 360px;
    box-shadow: 0 6px 18px rgba(0,0,0,0.18);
    overflow: hidden;
  }
  .card-back {
    top: 60px;
    background: linear-gradient(135deg, var(--brand-blue-light) 0%, var(--brand-blue) 55%, var(--brand-blue-dark) 100%);
    display: flex;
    align-items: center;
    justify-content: center;
  }
  .card-front {
    top: 480px;
    background: linear-gradient(160deg, var(--card-white) 0%, var(--card-white) 45%, var(--card-grey) 100%);
  }
  .brand-name {
    font-family: "Lato", "Gill Sans", sans-serif;
    font-weight: 400;
    text-transform: uppercase;
    letter-spacing: 0.12em;
    text-align: center;
    line-height: 1;
  }
  .card-back .brand-name { color: var(--card-white); font-size: 34px; }
  .card-front .brand-name {
    position: absolute;
    top: 58px;
    left: 0; right: 0;
    color: var(--brand-blue);
    font-size: 27px;
  }
  .contact-person {
    position: absolute;
    left: 40px;
    top: 160px;
  }
  .person-name {
    color: var(--brand-blue);
    font-size: 23px;
    font-weight: 400;
    text-transform: uppercase;
    letter-spacing: 0.02em;
  }
  .person-title {
    color: var(--ink);
    font-size: 14px;
    margin-top: 2px;
  }
  .contact-list {
    list-style: none;
    margin-top: 22px;
    font-size: 15px;
    color: var(--ink);
    line-height: 1.5;
  }
  .contact-list .label {
    display: inline-block;
    width: 18px;
    color: var(--brand-blue);
  }
  .address-block {
    position: absolute;
    left: 400px;
    top: 200px;
    padding-left: 12px;
    border-left: 1.5px solid var(--brand-blue);
    font-size: 14px;
    line-height: 1.45;
    color: var(--ink);
    height: 72px;
  }
  .address-block .web { color: var(--brand-blue); }
  .footer-band {
    position: absolute;
    left: 0; right: 0; bottom: 0;
    height: 44px;
    background: linear-gradient(90deg, var(--brand-blue) 0%, var(--brand-blue-dark) 100%);
  }
</style>
</head>
<body>
  <section class="card card-back" aria-label="Card back">
    <p class="brand-name">Highfield Catering Company</p>
  </section>

  <section class="card card-front" aria-label="Card front">
    <p class="brand-name">Highfield Catering Company</p>

    <div class="contact-person">
      <h1 class="person-name">Marisol Quedenfeldt</h1>
      <p class="person-title">catering director</p>
      <ul class="contact-list">
        <li><span class="label">p</span>407-555-0182</li>
        <li><span class="label">m</span>407-555-0267</li>
        <li><span class="label">e</span>marisol.t.quedenfeldt-1@orvanta-mail.org</li>
      </ul>
    </div>

    <address class="address-block" style="font-style: normal;">
      Building R2-718 PTX<br>
      Brightwater Launch Campus, Florida, 33741<br>
      <span class="web">www.highfieldcatering.com</span>
    </address>

    <div class="footer-band"></div>
  </section>
</body>
</html>
```